Business Card Design, including supply of raw art files plus a vector diagram of the zelvon logo and

We need the business card design for a company that is launching a new exciting product. The brief requires the submission of the following once the final design is chosen:

- business card layout including raw files
- a composite vector image file of the zelvon logo and tag line
- a standalone vector image file of the zelvon logo

The product will be launched as a customer engagement app.

It has 4 core modules which enables a person to do multiple things - book tours and activities, order takeaways, search for local deals and offers. A universal currency is at the heart of this product. When you use the app, you earn cashback rewards when shopping or buying at any of the merchant partners across the modules as . These rewards can then be used as full or part payment when buying goods or services at these merchant partners.

The business card must help us build the brand, communicate the benefit of the brand's key focus - the ability to earn and burn this universal cashback ccurrency - across the 4 modules - booking of tours and activities, ordering, searching for local deals and payment.

We would like the design to use the brand's blue colour the hex colour is: 00
Dark grey : 646464
Darker blue shadow: 058bdd
Main Blue: 0084ff

We need to translate this into a CMYK print or spot colour print.

Both print options to be supplied as separate files.

An example of the base concept we have in mind is attached for your reference.

The font used by the brand is Proxima Nova.

Note: the duration has been set as 2 days.

Industry/Entity Type

Business

Contact Information for Business Card

Carla Mendoza
Marketing
W: www.zelvon.example
M: + 61 400555123
T: +61 2 5550 1473
A: Suite 7, Level 2, 14-18 Harwick Street, Sydney, NSW, 2000, Australia

Font styles to use
Sans Serif

Requirements
Must have
• zelVon logo and tagline
• address details
• zelVon icons as supplied
Nice to have
• would like to have the option of a spot varnish layer over the logo and icons at the back of the card

```html
<!DOCTYPE html>
<html lang="en">
<head>
<meta charset="utf-8">
<title>zelvon business cards</title>
<link rel="stylesheet" href="https://fonts.googleapis.com/css2?family=Figtree:wght@300;400;700&display=swap">
<style>
  :root {
    --backdrop: #3b3b3b;
    --blue-deep: #3d7bc0;
    --blue-bright: #3ea3db;
    --brand-blue: #2b8fd6;
    --white: #ffffff;
    --grey-dark: #646464;
    --grey-text: #555555;
  }
  * { margin: 0; padding: 0; box-sizing: border-box; }
  html, body { width: 1200px; height: 1000px; overflow: hidden; }
  body {
    background: var(--backdrop);
    font-family: "Figtree", sans-serif;
    position: relative;
  }
  .card {
    position: absolute;
    width: 460px;
    height: 308px;
    border-radius: 8px;
    overflow: hidden;
    box-shadow: 0 6px 18px rgba(0,0,0,0.35);
  }
  .card--front-deep { left: 133px; top: 172px; background: var(--blue-deep); }
  .card--front-bright { left: 133px; top: 503px; background: var(--blue-bright); }
  .card--back { background: var(--white); }
  .card--back-top { left: 614px; top: 172px; }
  .card--back-bottom { left: 614px; top: 503px; }

  /* front */
  .brand-disc {
    position: absolute;
    left: 69px; top: 63px;
    width: 94px; height: 94px;
    border-radius: 50%;
    background: var(--white);
  }
  .brand-lockup {
    position: absolute;
    left: 184px; top: 72px;
    text-align: left;
    color: var(--white);
  }
  .brand-name {
    display: block;
    font-weight: 400;
    font-size: 56px;
    line-height: 1;
  }
  .brand-tagline {
    display: block;
    font-weight: 400;
    font-size: 17px;
    line-height: 1;
    margin-top: 6px;
  }
  .modules {
    position: absolute;
    left: 0; top: 227px;
    width: 100%;
    height: 50px;
  }
  .module {
    position: absolute;
    width: 84px;
    margin-left: -42px;
    text-align: center;
    color: var(--white);
  }
  .module svg { display: block; margin: 0 auto; width: 30px; height: 30px; }
  .module-label {
    display: block;
    font-size: 8px;
    font-weight: 700;
    margin-top: 4px;
    white-space: nowrap;
  }
  .module--cashback { left: 112px; }
  .module--tours { left: 198px; }
  .module--ordering { left: 281px; }
  .module--offers { left: 365px; }

  /* back */
  .back-disc {
    position: absolute;
    left: 238px; top: 48px;
    width: 50px; height: 50px;
    border-radius: 50%;
    background: var(--brand-blue);
  }
  .back-lockup {
    position: absolute;
    left: 298px; top: 50px;
    text-align: left;
    color: var(--grey-dark);
  }
  .back-name {
    display: block;
    font-weight: 400;
    font-size: 32px;
    line-height: 1;
  }
  .back-tagline {
    display: block;
    font-size: 11px;
    font-weight: 400;
    line-height: 1.3;
  }
  .back-web {
    position: absolute;
    right: 58px; top: 110px;
    color: var(--grey-dark);
    font-size: 15px;
    font-weight: 400;
  }
  .contact {
    position: absolute;
    left: 61px; top: 192px;
    color: var(--grey-text);
  }
  .contact-name {
    font-size: 19px;
    font-weight: 400;
    margin-bottom: 2px;
  }
  .contact-line {
    font-size: 12px;
    line-height: 17.5px;
    font-weight: 400;
  }
</style>
</head>
<body>

  <section class="card card--front-deep">
    <div class="brand-disc"></div>
    <div class="brand-lockup">
      <span class="brand-name">zelvon</span>
      <span class="brand-tagline">rewards made local</span>
    </div>
    <div class="modules">
      <div class="module module--cashback">
        <svg viewBox="0 0 30 30" aria-hidden="true">
          <path d="M4 11 A10 10 0 0 1 22 6" fill="none" stroke="#fff" stroke-width="2.5"/>
          <path d="M20 2 L24 7 L18 9 Z" fill="#fff"/>
          <path d="M26 19 A10 10 0 0 1 8 24" fill="none" stroke="#fff" stroke-width="2.5"/>
          <path d="M10 28 L6 23 L12 21 Z" fill="#fff"/>
          <circle cx="15" cy="15" r="6.5" fill="#fff"/>
          <text x="15" y="18.5" font-size="9" font-weight="700" text-anchor="middle" fill="var(--blue-deep)" font-family="Figtree, sans-serif">$</text>
        </svg>
        <span class="module-label">CashBack Rewards</span>
      </div>
      <div class="module module--tours">
        <svg viewBox="0 0 30 30" aria-hidden="true">
          <path d="M3 9 H10 L12 5 H18 L20 9 H27 V25 H3 Z" fill="#fff"/>
          <circle cx="15" cy="17" r="5.5" fill="var(--blue-deep)"/>
          <circle cx="15" cy="17" r="3.5" fill="#fff"/>
        </svg>
        <span class="module-label">Tours &amp; Activities</span>
      </div>
      <div class="module module--ordering">
        <svg viewBox="0 0 30 30" aria-hidden="true">
          <line x1="7" y1="4" x2="22" y2="27" stroke="#fff" stroke-width="2"/>
          <ellipse cx="21" cy="8" rx="3.5" ry="5" fill="#fff"/>
          <line x1="19" y1="12" x2="8" y2="27" stroke="#fff" stroke-width="2"/>
        </svg>
        <span class="module-label">Mobile Ordering</span>
      </div>
      <div class="module module--offers">
        <svg viewBox="0 0 30 30" aria-hidden="true"></svg>
        <span class="module-label">Local Offers</span>
      </div>
    </div>
  </section>

  <section class="card card--back card--back-top">
    <div class="back-disc"></div>
    <div class="back-lockup">
      <span class="back-name">zelvon</span>
      <span class="back-tagline">rewards made local</span>
    </div>
    <span class="back-web">www.zelvon.example</span>
    <div class="contact">
      <p class="contact-name">Carla Mendoza | Marketing</p>
      <p class="contact-line">&nbsp;E : carla@zelvon.example</p>
      <p class="contact-line">M :+ 61 400555123 | T: +61 2 5550 1473</p>
      <p class="contact-line">&nbsp;A :Suite 7, Level 2, 14-18 Harwick Street, Sydney NSW 2000</p>
    </div>
  </section>

  <section class="card card--front-bright">
    <div class="brand-disc"></div>
    <div class="brand-lockup">
      <span class="brand-name">zelvon</span>
      <span class="brand-tagline">rewards made local</span>
    </div>
    <div class="modules">
      <div class="module module--cashback">
        <svg viewBox="0 0 30 30" aria-hidden="true">
          <path d="M4 11 A10 10 0 0 1 22 6" fill="none" stroke="#fff" stroke-width="2.5"/>
          <path d="M20 2 L24 7 L18 9 Z" fill="#fff"/>
          <path d="M26 19 A10 10 0 0 1 8 24" fill="none" stroke="#fff" stroke-width="2.5"/>
          <path d="M10 28 L6 23 L12 21 Z" fill="#fff"/>
          <circle cx="15" cy="15" r="6.5" fill="#fff"/>
          <text x="15" y="18.5" font-size="9" font-weight="700" text-anchor="middle" fill="var(--blue-bright)" font-family="Figtree, sans-serif">$</text>
        </svg>
        <span class="module-label">CashBack Rewards</span>
      </div>
      <div class="module module--tours">
        <svg viewBox="0 0 30 30" aria-hidden="true">
          <path d="M3 9 H10 L12 5 H18 L20 9 H27 V25 H3 Z" fill="#fff"/>
          <circle cx="15" cy="17" r="5.5" fill="var(--blue-bright)"/>
          <circle cx="15" cy="17" r="3.5" fill="#fff"/>
        </svg>
        <span class="module-label">Tours &amp; Activities</span>
      </div>
      <div class="module module--ordering">
        <svg viewBox="0 0 30 30" aria-hidden="true">
          <line x1="7" y1="4" x2="22" y2="27" stroke="#fff" stroke-width="2"/>
          <ellipse cx="21" cy="8" rx="3.5" ry="5" fill="#fff"/>
          <line x1="19" y1="12" x2="8" y2="27" stroke="#fff" stroke-width="2"/>
        </svg>
        <span class="module-label">Mobile Ordering</span>
      </div>
      <div class="module module--offers">
        <svg viewBox="0 0 30 30" aria-hidden="true">
          <path d="M16 3 H26 V13 L13 26 L3 16 Z" fill="#fff"/>
          <circle cx="21.5" cy="7.5" r="2" fill="var(--blue-bright)"/>
        </svg>
        <span class="module-label">Local Offers</span>
      </div>
    </div>
  </section>

  <section class="card card--back card--back-bottom">
    <div class="back-disc"></div>
    <div class="back-lockup">
      <span class="back-name">zelvon</span>
      <span class="back-tagline">rewards made local</span>
    </div>
    <span class="back-web">www.zelvon.example</span>
    <div class="contact">
      <p class="contact-name">Carla Mendoza | Marketing</p>
      <p class="contact-line">&nbsp;E : carla@zelvon.example</p>
      <p class="contact-line">M :+ 61 400555123 | T: +61 2 5550 1473</p>
      <p class="contact-line">&nbsp;A :Suite 7, Level 2, 14-18 Harwick Street, Sydney NSW 2000</p>
    </div>
  </section>

</body>
</html>
```